A3 Event Poster for School Fundraiser

We are looking for a bold, engaging, and professional A3 poster design to promote a special school fundraising event. A top athlete will be visiting a primary school to inspire children, encourage participation in sport, and help launch a fundraising initiative to raise money for new PE/sports equipment for the school.

The poster will be displayed prominently outside the school and shared with parents and families. Its purpose is to generate excitement, explain the event quickly, and encourage parents/families to sponsor and get involved.

We work with about 50 different athletes so will need the design to be easy to alter the picture of the athlete/name etc so it can be replicated across the different athletes.

Target Market(s)

Priamary School Parents/Communities

Industry/Entity Type

Education

Font styles to use
Other font styles liked:
• The logo font is Rajdhani. ‘Corvel’ is bold, ‘Pennix’ is semibold and the strapline is regular.

Requirements
Must have
• Space for the Event Date (that school can write in themselves), A picture of the visiting athlete and their bio (with ability to easily change)
Nice to have
• Bold, eye-catching

```html
<!DOCTYPE html>
<html lang="en">
<head>
<meta charset="utf-8">
<title>Corvel Pennix – Athlete School Visit Poster</title>
<link rel="stylesheet" href="https://fonts.googleapis.com/css2?family=Rajdhani:wght@400;500;600;700&family=Montserrat:wght@600;800;900&display=swap">
<style>
  :root {
    --purple: #6a2a7e;
    --red: #e31b36;
    --white: #ffffff;
    --page: #dedede;
    --orange-top: #fbb32a;
    --orange-bottom: #f26a1f;
  }
  * { margin: 0; padding: 0; box-sizing: border-box; }
  html, body { width: 930px; height: 1200px; overflow: hidden; background: var(--page); }
  body { font-family: "Rajdhani", sans-serif; }

  .poster {
    position: absolute; left: 65px; top: 0;
    width: 800px; height: 1200px;
    background: var(--white); overflow: hidden;
  }
  .poster > * { position: absolute; }

  /* Header / brand */
  .brand {
    left: 0; top: 0; width: 800px; height: 115px;
    display: flex; align-items: center; justify-content: center; gap: 10px;
  }
  .brand-mark { width: 34px; height: 34px; border-radius: 50%; background: var(--red); flex: none; }
  .brand-text { display: flex; flex-direction: column; line-height: 1; }
  .brand-name { font-weight: 600; font-size: 46px; color: var(--purple); letter-spacing: 1px; }
  .brand-strap { font-weight: 400; font-size: 15px; color: var(--purple); margin-top: 2px; }

  /* Purple field */
  .field { left: 0; top: 115px; width: 800px; height: 891px; background: var(--purple); }

  .athlete-photo {
    left: 497px; top: 97px; width: 303px; height: 523px;
    background: linear-gradient(180deg, #3b2a2e 0%, #2b3f8f 45%, #c93a4a 65%, var(--purple) 100%);
    -webkit-mask-image: linear-gradient(180deg, #000 70%, transparent 100%);
            mask-image: linear-gradient(180deg, #000 70%, transparent 100%);
    border-radius: 140px 0 0 0;
  }

  .headline {
    left: 40px; top: 140px; width: 420px;
    font-weight: 700; color: var(--white); line-height: 1;
    text-shadow: 0 3px 4px rgba(0,0,0,.25);
  }
  .headline span { display: block; }
  .headline .l1 { font-size: 76px; height: 80px; }
  .headline .l2 { font-size: 124px; height: 104px; color: var(--red); line-height: 0.8; padding-top: 4px; }
  .headline .l3 { font-size: 86px; height: 86px; line-height: 0.95; }
  .headline .l4 { font-size: 152px; line-height: 0.85; }

  .role-pill {
    left: 40px; top: 558px; width: 518px; height: 62px;
    background: var(--red); border-radius: 14px;
    display: flex; align-items: center; justify-content: center;
    font-weight: 700; font-size: 44px; color: var(--white);
    box-shadow: 0 3px 0 rgba(0,0,0,.2);
  }

  .bio {
    left: 42px; top: 628px; width: 519px;
    font-weight: 500; font-size: 21px; line-height: 26.6px;
    color: var(--white); text-align: justify;
  }

  .appeal {
    left: 46px; top: 752px;
    font-weight: 700; font-size: 31px; line-height: 37.6px;
    color: var(--white); text-transform: uppercase;
  }

  .actions { left: 259px; top: 736px; width: 299px; }
  .action {
    height: 50px; margin-bottom: 11px; padding-left: 15px;
    background: var(--red); border-radius: 9px;
    display: flex; align-items: center;
    font-weight: 700; font-size: 35px; color: var(--white);
    box-shadow: 0 3px 0 rgba(0,0,0,.25);
  }

  .event-date { left: 613px; top: 635px; width: 155px; text-align: center; }
  .date-label {
    height: 30px; border-radius: 15px; background: var(--red);
    font-weight: 700; font-size: 25px; line-height: 31px; color: var(--white);
  }
  .date-year, .date-day {
    font-family: "Montserrat", sans-serif; font-weight: 900;
    background: linear-gradient(180deg, var(--orange-top), var(--orange-bottom));
    -webkit-background-clip: text; background-clip: text; color: transparent;
  }
  .date-year { font-size: 40px; line-height: 40px; height: 38px; margin-top: 14px; letter-spacing: 1px; }
  .date-month {
    font-family: "Montserrat", sans-serif; font-weight: 900;
    font-size: 34px; line-height: 40px; height: 40px; color: var(--white); letter-spacing: -1px;
  }
  .date-day { font-size: 140px; line-height: 112px; height: 112px; letter-spacing: -8px; padding-right: 8px; }
  .date-time {
    width: 150px; height: 31px; margin: 2px 0 0 0;
    border-top: 3px solid var(--red); background: var(--red);
    font-family: "Montserrat", sans-serif; font-weight: 600;
    font-size: 13.5px; line-height: 27px; color: var(--white);
  }

  /* Gallery */
  .gallery-photo { top: 954px; width: 238px; height: 191px; border-radius: 3px; }
  .gallery-photo.one { left: 33px; background: linear-gradient(135deg, #3aa874 0%, #d8a772 55%, #b8864e 100%); }
  .gallery-photo.two { left: 285px; background: linear-gradient(135deg, #d9c9a8 0%, #c84a3a 55%, #6b4a34 100%); }
  .gallery-photo.three { left: 537px; background: linear-gradient(135deg, #caa67a 0%, #e7e1dc 50%, #cc2b2b 100%); }

  .tagline {
    left: 0; top: 1153px; width: 800px;
    text-align: center; font-weight: 700; font-size: 25px; color: var(--red);
  }
</style>
</head>
<body>
  <main class="poster">
    <header class="brand">
      <span class="brand-mark" aria-hidden="true"></span>
      <div class="brand-text">
        <span class="brand-name">CorvelPennix</span>
        <span class="brand-strap">Inspiring every child</span>
      </div>
    </header>

    <div class="field" aria-hidden="true"></div>

    <div class="athlete-photo" role="img" aria-label="Portrait of the visiting volleyball athlete wearing a red, white and blue team jacket"></div>

    <h1 class="headline">
      <span class="l1">Inspirational</span>
      <span class="l2">Athlete</span>
      <span class="l3">Visiting Our</span>
      <span class="l4">School</span>
    </h1>

    <div class="role-pill">Olympic Volleyball Player</div>

    <p class="bio">Dorian is a dynamic English volleyball player and coach, known for his leadership on and off the court and his passion for inspiring the next generation through sport.</p>

    <p class="appeal">Help us raise<br>funds for<br>new sports<br>equipment</p>

    <div class="actions">
      <div class="action">Be Inspired</div>
      <div class="action">Make a Difference</div>
      <div class="action">Get Active</div>
    </div>

    <div class="event-date">
      <div class="date-label">EVENT DATE</div>
      <div class="date-year">2026</div>
      <div class="date-month">AUGUST</div>
      <div class="date-day">16</div>
      <div class="date-time">4:00 PM - 7:30 PM</div>
    </div>

    <div class="gallery-photo one" role="img" aria-label="Children doing push-ups in a school hall"></div>
    <div class="gallery-photo two" role="img" aria-label="Wheelchair athlete leading a group of pupils in an exercise session"></div>
    <div class="gallery-photo three" role="img" aria-label="Smiling athlete posing with a young pupil in a classroom"></div>

    <p class="tagline">Inspiring every child to lead an active, resilient and healthy life</p>
  </main>
</body>
</html>
```